Chatterly News Feed Advertisement for Bitcoin Startup

CoinHarbor is a bitcoin brokerage in South Africa.
We need an advertisement for our Chatterly newsfeed.
Modern, technology feel to the advertisement.
Colours should compliment our logo in the attached document
Advertisement text: "The cheapest Bitcoin in South Africa"
Creative hints: Include an image of a bitcoin. Include something visual relating to South Africa (map, flag etc.). These are just hints an do not need to be followed to the letter, we appreciate creative freedom.
Updates

Project Deadline Extended Reason: This advertisement will only be needed on 10th May. Added Monday, April 24, 2017

Target Market(s)

People wanting to purchase bitcoin

Industry/Entity Type

News

Font styles to use
Sans Serif

Colors

Designer to choose colors to be used in the design.

Requirements
Must have
• Size: 1000 x 561 pixels (landscape)
• Text must not constitute more than 20% of the design (as per Chatterly requirements0
Nice to have
• Attached is our logo for your reference. Creative freedom is yours.
Should not have
• No preferences

Files

```html
<!DOCTYPE html>
<html lang="en">
<head>
<meta charset="utf-8">
<title>CoinHarbor – The cheapest bitcoin in South Africa</title>
<link rel="stylesheet" href="https://fonts.googleapis.com/css2?family=Open+Sans:wght@700;800&display=swap">
<style>
  :root {
    --navy: #00326a;
    --tone-green: #007a4d;
    --tone-gold: #f99c00;
    --tone-red: #e03c31;
    --white: #ffffff;
    --accent: #f99c00;
  }
  html, body {
    margin: 0;
    padding: 0;
    width: 1200px;
    height: 673px;
    overflow: hidden;
    background: var(--navy);
  }
  .ad {
    position: relative;
    width: 1200px;
    height: 673px;
    overflow: hidden;
    font-family: "Open Sans", Arial, sans-serif;
  }
  .ad__backdrop {
    position: absolute;
    inset: 0;
    display: block;
  }
  .panel-navy { fill: var(--navy); }
  .flag-area { fill: url(#flagTones); }

  .headline {
    position: absolute;
    left: 714px;
    top: 232px;
    margin: 0;
    color: var(--white);
    font-weight: 800;
    font-size: 48px;
    line-height: 55px;
    letter-spacing: 0.4px;
  }
  .headline__accent { color: var(--accent); }

  .brand {
    position: absolute;
    right: 34px;
    bottom: 34px;
    display: flex;
    align-items: center;
    gap: 16px;
    color: var(--white);
    font-weight: 700;
    font-size: 27px;
    line-height: 1;
  }
  .brand__dot {
    width: 34px;
    height: 34px;
    border-radius: 50%;
    background: var(--accent);
  }
</style>
</head>
<body>
  <main class="ad">
    <svg class="ad__backdrop" width="1200" height="673" viewBox="0 0 1000 561" preserveAspectRatio="none">
      <defs>
        <linearGradient id="flagTones" x1="0" y1="1" x2="1" y2="0">
          <stop offset="0" stop-color="#007a4d"/>
          <stop offset="0.55" stop-color="#4d8a3a"/>
          <stop offset="1" stop-color="#e03c31"/>
        </linearGradient>
      </defs>
      <rect class="panel-navy" x="0" y="0" width="1000" height="561"/>
      <polygon class="flag-area" role="img" aria-label="South African flag" points="0,0 610,0 290,561 0,561"/>
    </svg>

    <h1 class="headline">
      the <span class="headline__accent">cheapest</span><br>
      <span class="headline__accent">bitcoin</span> in<br>
      South Africa
    </h1>

    <div class="brand">
      <span class="brand__dot"></span>
      <span class="brand__name">CoinHarbor</span>
    </div>
  </main>
</body>
</html>
```